Decorative Envelope That Encases Package

Hello All,
I have a small envelope that is going to hold a trial sample of a high end supplement.
I want this envelope to look like a Gold Treasure Chest
I want to try to make it as 3D as possible. Please utilize all sides.
I would like it around 90% done. I want you to leave room for our logo and some icons. (We can put them on later)
We are going to use a Gold Metallic color and the Pantone is 10122 C
If you are going to put anything on there like jewelry please make it green and use the Pantone 10309 C
Our product is a supplement. It is called Mirela Seagrain and the website is www.themirelaventure.example for reference.
Updates

Hello All,
I am getting messages a lot of you can't see the website for security reasons. You honestly don't have to worry about it. I just need the envelope to look like a 3D Treasure Chest.
Hope this helps

```html
<!DOCTYPE html>
<html lang="en">
<head>
<meta charset="utf-8">
<title>Treasure Chest Envelope Dieline</title>
<link rel="stylesheet" href="https://fonts.googleapis.com/css2?family=Cinzel:wght@600&display=swap">
<style>
  :root {
    --paper: #ffffff;
    --cut-line: #e0308f;
    --wood-light: #b87049;
    --wood-mid: #9c5733;
    --wood-dark: #6e3a20;
    --gold-light: #f6e4a4;
    --gold: #dcbc68;
    --gold-deep: #b8913e;
    --rivet: #9a7630;
  }
  html, body {
    margin: 0;
    padding: 0;
    width: 1200px;
    height: 2330px;
    overflow: hidden;
    background: var(--paper);
    font-family: "Cinzel", serif;
  }
  .envelope {
    display: block;
    width: 1200px;
    height: 2330px;
  }
  .cut { fill: none; stroke: var(--cut-line); stroke-width: 2; }
  .wood { fill: url(#woodGrain); }
  .wood-side { fill: url(#woodSide); }
  .gold { fill: url(#goldBand); stroke: var(--gold-deep); stroke-width: 2; }
  .gold-v { fill: url(#goldBandV); stroke: var(--gold-deep); stroke-width: 2; }
  .corner { fill: var(--gold); stroke: var(--gold-deep); stroke-width: 2; }
  .rivets {
    fill: none;
    stroke: var(--rivet);
    stroke-width: 9;
    stroke-linecap: round;
    stroke-dasharray: 0 38;
  }
  .keyhole { fill: var(--wood-dark); }
</style>
</head>
<body>
<svg class="envelope" viewBox="0 0 1200 2330" xmlns="http://www.w3.org/2000/svg">
  <defs>
    <linearGradient id="woodGrain" x1="0" y1="0" x2="1" y2="0">
      <stop offset="0" stop-color="var(--wood-mid)"/>
      <stop offset="0.35" stop-color="var(--wood-light)"/>
      <stop offset="0.65" stop-color="var(--wood-mid)"/>
      <stop offset="1" stop-color="var(--wood-light)"/>
    </linearGradient>
    <linearGradient id="woodSide" x1="0" y1="0" x2="1" y2="0">
      <stop offset="0" stop-color="var(--wood-dark)"/>
      <stop offset="1" stop-color="var(--wood-mid)"/>
    </linearGradient>
    <linearGradient id="goldBand" x1="0" y1="0" x2="0" y2="1">
      <stop offset="0" stop-color="var(--gold-light)"/>
      <stop offset="0.5" stop-color="var(--gold)"/>
      <stop offset="1" stop-color="var(--gold-deep)"/>
    </linearGradient>
    <linearGradient id="goldBandV" x1="0" y1="0" x2="1" y2="0">
      <stop offset="0" stop-color="var(--gold-deep)"/>
      <stop offset="0.45" stop-color="var(--gold-light)"/>
      <stop offset="1" stop-color="var(--gold)"/>
    </linearGradient>
  </defs>

  <!-- Lid flap -->
  <g class="lid-flap">
    <polygon class="gold-v" points="211,53 262,112 955,112 1010,53 1010,1039 211,1039"/>
    <path class="wood" role="img" aria-label="Wood grain texture of the chest lid"
          d="M249 1010 V160 Q249 112 297 112 H918 Q966 112 966 160 V1010 Z"/>
    <rect class="gold-v" x="240" y="150" width="42" height="860"/>
    <rect class="gold-v" x="935" y="150" width="42" height="860"/>
    <line class="rivets" x1="261" y1="180" x2="261" y2="950"/>
    <line class="rivets" x1="956" y1="180" x2="956" y2="950"/>
    <rect class="gold" x="211" y="960" width="799" height="52"/>
    <line class="rivets" x1="300" y1="986" x2="920" y2="986"/>
    <rect class="corner" x="240" y="120" width="80" height="80" rx="14"/>
    <rect class="corner" x="897" y="120" width="80" height="80" rx="14"/>
    <rect class="corner" x="230" y="900" width="95" height="110" rx="16"/>
    <rect class="corner" x="892" y="900" width="95" height="110" rx="16"/>
    <!-- padlock -->
    <g class="padlock">
      <path d="M566 240 V210 Q566 176 600 176 Q634 176 634 210 V240" fill="none" stroke="var(--gold-deep)" stroke-width="12"/>
      <rect class="corner" x="546" y="235" width="108" height="80" rx="16"/>
      <circle class="keyhole" cx="600" cy="268" r="9"/>
      <rect class="keyhole" x="596" y="270" width="8" height="24" rx="3"/>
    </g>
  </g>

  <!-- Hinge band -->
  <rect class="gold" x="211" y="1012" width="799" height="62"/>
  <line class="rivets" x1="240" y1="1043" x2="990" y2="1043"/>

  <!-- Side flaps -->
  <polygon class="wood-side" role="img" aria-label="Wood grain texture of left side flap" points="117,1075 211,1045 211,2015 117,1985"/>
  <polygon class="wood-side" role="img" aria-label="Wood grain texture of right side flap" points="1098,1075 1010,1045 1010,2015 1098,1985"/>
  <polygon class="cut" points="117,1075 211,1045 211,2015 117,1985"/>
  <polygon class="cut" points="1098,1075 1010,1045 1010,2015 1098,1985"/>

  <!-- Front panel -->
  <g class="front-panel">
    <rect class="wood" role="img" aria-label="Wood grain texture of the chest front" x="211" y="1074" width="799" height="946"/>
    <rect class="gold" x="211" y="1074" width="799" height="52"/>
    <line class="rivets" x1="300" y1="1100" x2="920" y2="1100"/>
    <rect class="gold-v" x="211" y="1074" width="56" height="946"/>
    <rect class="gold-v" x="954" y="1074" width="56" height="946"/>
    <line class="rivets" x1="239" y1="1160" x2="239" y2="1950"/>
    <line class="rivets" x1="982" y1="1160" x2="982" y2="1950"/>
    <rect class="gold" x="211" y="1955" width="799" height="65"/>
    <line class="rivets" x1="260" y1="1987" x2="960" y2="1987"/>
    <rect class="gold-v" x="566" y="1126" width="68" height="830"/>
    <line class="rivets" x1="600" y1="1160" x2="600" y2="1930"/>
    <rect class="corner" x="211" y="1074" width="120" height="110" rx="18"/>
    <rect class="corner" x="890" y="1074" width="120" height="110" rx="18"/>
    <rect class="corner" x="211" y="1870" width="120" height="150" rx="18"/>
    <rect class="corner" x="890" y="1870" width="120" height="150" rx="18"/>
  </g>

  <!-- Bottom flap -->
  <g class="bottom-flap">
    <path class="wood" role="img" aria-label="Wood grain texture of the bottom flap"
          d="M263 2020 H966 V2200 Q966 2283 880 2283 H350 Q263 2283 263 2200 Z"/>
    <path class="gold" d="M263 2020 H966 L940 2120 Q900 2085 860 2080 H360 Q320 2085 290 2120 Z"/>
    <line class="rivets" x1="330" y1="2048" x2="880" y2="2048"/>
    <rect class="corner" x="555" y="1960" width="90" height="260" rx="30"/>
    <rect class="keyhole" x="590" y="2150" width="20" height="50" rx="10"/>
    <path class="cut" d="M263 2020 V2200 Q263 2283 350 2283 H880 Q966 2283 966 2200 V2020"/>
  </g>

  <!-- Outline of lid and body -->
  <polyline class="cut" points="211,2020 211,53 262,112 955,112 1010,53 1010,2020"/>
</svg>
</body>
</html>
```